A web page that is on trend and quite random

Hi,

We require a super basic website. We think we will just keep it black and white. We will require the menu and location to appear on the page.

Our menu will be requiring some basic changes so a format that we easily change it is preferred. Please subtly include the clock as it is our logo?

SEO would be great.

```html
<!DOCTYPE html>
<html lang="en">
<head>
<meta charset="utf-8">
<title>the Fox &amp; Heron — Café Menu &amp; Location</title>
<meta name="description" content="the Fox & Heron café: organic eggs, free range meat and sourdough baked daily. View our menu.">
<meta name="viewport" content="width=788">
<link rel="stylesheet" href="https://fonts.googleapis.com/css2?family=Playfair+Display:wght@700&family=Dancing+Script:wght@600&family=Satisfy&display=swap">
<style>
  :root {
    --ink: #1a1a1a;
    --paper: #ffffff;
    --rule: #9a9a9a;
    --card-border: #bdbdbd;
    --muted: #555555;
    --footer: #000000;
  }
  * { box-sizing: border-box; margin: 0; padding: 0; }
  html, body { width: 788px; height: 1200px; overflow: hidden; background: var(--paper); }
  body { position: relative; color: var(--ink); font-family: "Satisfy", cursive; }

  .site-header {
    position: absolute; top: 0; left: 0; width: 788px; height: 58px;
    display: flex; align-items: center; justify-content: center;
  }
  .brand {
    font-family: "Playfair Display", serif; font-weight: 700;
    font-size: 26px; color: var(--ink); letter-spacing: 0.2px;
  }
  .site-footer .brand { color: var(--paper); }

  .hero {
    position: absolute; top: 58px; left: 0; width: 788px; height: 324px;
    background: radial-gradient(ellipse at 38% 55%, #c9a77a 0%, #a0602e 28%, #d49a3a 48%, #3b2a20 80%, #1e1714 100%);
  }

  .about {
    position: absolute; top: 398px; left: 47px; width: 695px; height: 140px;
  }
  .about-mark {
    position: absolute; left: 0; top: 4px; width: 62px; height: 62px;
    border: 4px solid var(--ink); border-radius: 50%;
  }
  .about-title {
    position: absolute; left: 95px; top: 4px;
    font-family: "Dancing Script", cursive; font-weight: 600; font-size: 27px;
    display: flex; align-items: center; width: 600px;
  }
  .about-title::after {
    content: ""; flex: 1; height: 1px; background: var(--rule); margin-left: 14px;
  }
  .about-text {
    position: absolute; left: 95px; top: 52px; width: 590px;
    font-size: 14px; line-height: 19px; color: var(--muted);
  }

  .menu { position: absolute; top: 560px; left: 47px; width: 695px; }
  .menu-item {
    position: relative; height: 120px; margin-bottom: 20px;
    border: 1px solid var(--card-border);
    box-shadow: 0 1px 3px rgba(0,0,0,0.15);
  }
  .menu-photo {
    position: absolute; left: 18px; top: 17px; width: 172px; height: 86px;
    background: linear-gradient(90deg, #9fb58a 0%, #d8cfa6 45%, #e6b55a 70%, #f0d08a 100%);
  }
  .menu-name {
    position: absolute; left: 222px; top: 26px; width: 450px;
    font-size: 15px; line-height: 21px;
  }
  .menu-line { display: flex; align-items: baseline; }
  .leader { flex: 1; border-bottom: 1px dotted var(--rule); margin: 0 8px; transform: translateY(-4px); }
  .price { font-size: 14px; }
  .menu-option {
    position: absolute; left: 222px; top: 80px; font-size: 12px; color: var(--muted);
    display: flex; align-items: baseline; width: 220px;
  }

  .site-footer {
    position: absolute; left: 0; top: 1118px; width: 788px; height: 82px;
    background: var(--footer);
  }
  .site-footer .brand { position: absolute; left: 42px; top: 22px; }
  .footer-mark {
    position: absolute; right: 98px; top: 26px; width: 28px; height: 28px;
    border: 3px solid var(--paper); border-radius: 50%;
  }
</style>
</head>
<body>
  <header class="site-header">
    <span class="brand">the Fox &amp; Heron</span>
  </header>

  <div class="hero" role="img" aria-label="Photo of a baked pie in a terracotta dish with bread rolls on a wooden board"></div>

  <section class="about">
    <span class="about-mark" aria-hidden="true"></span>
    <h1 class="about-title">About Us</h1>
    <p class="about-text">At The Fox &amp; Heron all our eggs are organic. Our meat is free range &amp; organic where possible. Breads are sourdough, baked daily by Ollie. See front counter for daily sweet selection.</p>
  </section>

  <main class="menu">
    <article class="menu-item">
      <div class="menu-photo" role="img" aria-label="Photo of a pie and side salad"></div>
      <div class="menu-name">Ollie's toasted sourdough with
        <div class="menu-line">Creamfield butter &amp; spreads<span class="leader"></span><span class="price">$6</span></div>
      </div>
      <div class="menu-option">(Mae's Gluten free also available)<span class="leader"></span>+$1</div>
    </article>
    <article class="menu-item">
      <div class="menu-photo" role="img" aria-label="Photo of a pie and side salad"></div>
      <div class="menu-name">Ollie's toasted sourdough with
        <div class="menu-line">Creamfield butter &amp; spreads<span class="leader"></span><span class="price">$6</span></div>
      </div>
      <div class="menu-option">(Mae's Gluten free also available)<span class="leader"></span>+$1</div>
    </article>
    <article class="menu-item">
      <div class="menu-photo" role="img" aria-label="Photo of a pie and side salad"></div>
      <div class="menu-name">Ollie's toasted sourdough with
        <div class="menu-line">Creamfield butter &amp; spreads<span class="leader"></span><span class="price">$6</span></div>
      </div>
      <div class="menu-option">(Mae's Gluten free also available)<span class="leader"></span>+$1</div>
    </article>
    <article class="menu-item">
      <div class="menu-photo" role="img" aria-label="Photo of a pie and side salad"></div>
      <div class="menu-name">Ollie's toasted sourdough with
        <div class="menu-line">Creamfield butter &amp; spreads<span class="leader"></span><span class="price">$6</span></div>
      </div>
      <div class="menu-option">(Mae's Gluten free also available)<span class="leader"></span>+$1</div>
    </article>
  </main>

  <footer class="site-footer">
    <span class="brand">the Fox &amp; Heron</span>
    <span class="footer-mark" aria-hidden="true"></span>
  </footer>
</body>
</html>
```